Design a Website Mockup for a Restaurant

In the moodboard you can find all the information you need to design the website. In the link below you can find the references of website that i think it is nice: https://www.filecrate-share.com/sh/wkz4pl8rtn2vd7/--_3Hmx8bq

I need responsive website, therefore please design also website mockup for iphone, ipad....

Facebook : https://www.socialnook-pages.com/pages/Marlow-Harbor-Kitchen-GmbH/481726095331864?fref=ts

```html
<!DOCTYPE html>
<html lang="de">
<head>
<meta charset="utf-8">
<title>Marlow – Restaurant</title>
<link rel="stylesheet" href="https://fonts.googleapis.com/css2?family=Oswald:wght@400;500;600&display=swap">
<style>
  :root {
    --brand-red: #e5372a;
    --ink: #1f1f1f;
    --sidebar-bg: #f3f2f0;
    --footer-bg: #1c1c1c;
    --footer-ink: #e9e9e9;
    --rule: #9a9a9a;
    --hero-warm: #8a4a2e;
    --hero-deep: #3a2a24;
    --white: #ffffff;
  }
  * { box-sizing: border-box; margin: 0; padding: 0; }
  html, body { width: 1200px; height: 800px; overflow: hidden; background: #dcdcdc; }
  body { font-family: "Oswald", "Arial Narrow", sans-serif; }

  .site {
    position: relative;
    width: 1200px;
    height: 800px;
    display: flex;
  }

  /* Sidebar */
  .sidebar {
    position: relative;
    width: 325px;
    height: 800px;
    flex: none;
    background: var(--sidebar-bg);
    display: flex;
    flex-direction: column;
    align-items: center;
  }
  .brand {
    margin-top: 52px;
    align-self: flex-start;
    margin-left: 70px;
    font-weight: 600;
    font-size: 38px;
    letter-spacing: 2px;
    color: var(--brand-red);
  }
  .main-nav {
    margin-top: 50px;
    list-style: none;
    width: 180px;
  }
  .main-nav li {
    text-align: center;
    font-size: 19px;
    font-weight: 500;
    color: var(--ink);
    letter-spacing: 0.5px;
    line-height: 40px;
    border-bottom: 2px dotted var(--rule);
  }
  .social {
    margin-top: 22px;
    display: flex;
    gap: 22px;
  }
  .social span {
    display: block;
    width: 34px;
    height: 34px;
    border-radius: 50%;
    background: var(--brand-red);
  }
  .legal {
    position: absolute;
    left: 0;
    bottom: 0;
    width: 100%;
    height: 140px;
    background: var(--footer-bg);
    display: flex;
    flex-direction: column;
    align-items: center;
    justify-content: center;
  }
  .legal a {
    color: var(--footer-ink);
    text-decoration: none;
    font-size: 19px;
    font-weight: 500;
    letter-spacing: 0.5px;
    width: 180px;
    text-align: center;
    line-height: 46px;
  }
  .legal a + a { border-top: 1px solid #555; }

  /* Hero */
  .hero {
    position: relative;
    flex: 1;
    height: 800px;
    overflow: hidden;
  }
  .hero-photo {
    position: absolute;
    inset: 0;
    background:
      radial-gradient(ellipse at 40% 30%, rgba(220,170,120,0.55), transparent 60%),
      linear-gradient(160deg, var(--hero-warm) 0%, #6e4a3a 45%, var(--hero-deep) 100%);
  }
  .slider-controls {
    position: absolute;
    top: 28px;
    right: 40px;
    display: flex;
    gap: 32px;
  }
  .slider-controls span {
    width: 40px;
    height: 42px;
    background: var(--white);
    display: flex;
    align-items: center;
    justify-content: center;
  }
  .headline, .subline {
    position: absolute;
    background: var(--brand-red);
    color: var(--white);
    font-weight: 500;
    white-space: nowrap;
    transform: rotate(-1.2deg);
    transform-origin: left center;
  }
  .headline {
    left: 60px;
    top: 300px;
    height: 48px;
    padding: 0 16px;
    font-size: 24px;
    line-height: 48px;
    letter-spacing: 0.5px;
  }
  .subline {
    left: 300px;
    top: 372px;
    height: 38px;
    padding: 0 12px;
    font-size: 17px;
    line-height: 38px;
    letter-spacing: 0.5px;
  }
</style>
</head>
<body>
  <div class="site">
    <aside class="sidebar">
      <div class="brand">MARLOW</div>
      <ul class="main-nav">
        <li>FILIALEN/ STORES</li>
        <li>SPEISEKARTE</li>
        <li>MEDIA</li>
        <li>RESEVIERUNG</li>
        <li>GUTSCHEINE</li>
        <li>NEUIGKEITEN/BLOGS</li>
      </ul>
      <div class="social" aria-label="Soziale Netzwerke">
        <span aria-label="Netzwerk 1"></span>
        <span aria-label="Netzwerk 2"></span>
        <span aria-label="Netzwerk 3"></span>
      </div>
      <nav class="legal">
        <a href="#">DATENSCHUTZ</a>
        <a href="#">IMPRESSUM</a>
      </nav>
    </aside>

    <main class="hero">
      <div class="hero-photo" role="img" aria-label="Foto des Restaurant-Innenraums mit Gästen, roten Lampen, Tischen und Sushi-Theke"></div>
      <div class="slider-controls">
        <span aria-label="Zurück">
          <svg width="12" height="18" viewBox="0 0 12 18"><path d="M10 2 L3 9 L10 16" fill="none" stroke="#1f1f1f" stroke-width="2.5"/></svg>
        </span>
        <span aria-label="Weiter">
          <svg width="12" height="18" viewBox="0 0 12 18"><path d="M2 2 L9 9 L2 16" fill="none" stroke="#1f1f1f" stroke-width="2.5"/></svg>
        </span>
      </div>
      <h1 class="headline">PROBIEREN SIE UNSEREN NEUEN SUSHI TELLER VON ALLES NEUE MENÜ</h1>
      <p class="subline">ERHÄLTLICH IN AUSGEWÄHLTEN RESTAURANTS</p>
    </main>
  </div>
</body>
</html>
```